High-end construction company needs a business card design

We need a modern looking business card that draws people in, is memorable and looks so good people will want to sick it on their fridges.
On the first side what is needed are:
Logo
My name - Tomas Verbelk
Title - Managing Director
Website - www.kravel.co.uk
Email - tomas@kravel.co.uk
Telephone - 020 5194 6381
Mobile - 07845319027
On the back side was is needed is a list of all the services we provide:
-Kitchen Renovations
-Bathroom Renovations
-House Renovations
-Garage Conversions
-Extensions
-Loft Conversions
-Conservatories
-Carpentry
-Tiling
-Electrical
-Plumbing & Heating
-Bricklaying
-Landscaping
-Decorating
-Plastering
We would like the colours to be the same shades as on the logo with grey or black for the words.
Target Market(s)
Anyone who needs building work done
Contact Information for Business Card
This business card is for a construction company which strives to deliver excellent service and quality.
The look and feel of the card should represent this.
Requirements
Must have
- On the first side what is needed are:
Logo
My name - Tomas Verbelk
Title - Managing Director
Website - www.kravel.co.uk
Email - tomas@kravel.co.uk
Telephone - 020 5194 6381
Mobile - 07845319027
Nice to have
- Cool looking features

```html
<!DOCTYPE html>
<html lang="en">
<head>
<meta charset="utf-8">
<title>Kravel Construction Ltd – Business Card</title>
<link href="https://fonts.googleapis.com/css2?family=Montserrat:wght@400;700;800&display=swap" rel="stylesheet">
<style>
  :root {
    --canvas: #c8c3c2;
    --card-edge: #0c1540;
    --card-panel: #120f3a;
    --green: #3ec44a;
    --white: #ffffff;
    --frame-line: #2e4a4a;
  }
  * { box-sizing: border-box; margin: 0; padding: 0; }
  html, body { width: 1200px; height: 1200px; overflow: hidden; }
  body {
    background: var(--canvas);
    font-family: "Montserrat", sans-serif;
    position: relative;
  }
  .card {
    position: absolute;
    background: var(--card-edge);
  }
  .card__panel {
    position: absolute;
    inset: 32px;
    background: var(--card-panel);
  }
  .card--front { left: 166px; top: 71px; width: 869px; height: 497px; }
  .card--back  { left: 176px; top: 638px; width: 849px; height: 486px; }

  /* front */
  .brand { position: absolute; left: 92px; top: 250px; color: var(--green); }
  .brand__name {
    display: flex; align-items: center; gap: 14px;
    font-weight: 800; font-size: 78px; line-height: 1; letter-spacing: 1px;
  }
  .brand__dot { width: 22px; height: 22px; border-radius: 50%; background: var(--green); }
  .brand__tagline {
    margin-top: 10px; font-weight: 800; font-size: 21px; letter-spacing: 3.6px;
  }
  .person { position: absolute; left: 501px; top: 92px; text-align: center; width: 290px; }
  .person__name { color: var(--green); font-weight: 700; font-size: 29px; letter-spacing: 2.5px; white-space: nowrap; }
  .person__title { color: var(--white); font-weight: 400; font-size: 23px; margin-top: 6px; white-space: nowrap; }
  .contacts { position: absolute; left: 500px; top: 193px; list-style: none; }
  .contact { display: flex; align-items: center; height: 43px; margin-bottom: 17px; }
  .contact__icon {
    width: 43px; height: 43px; border-radius: 50%; background: var(--green);
    display: flex; align-items: center; justify-content: center; flex: none;
  }
  .contact__text { margin-left: 26px; color: var(--green); font-size: 26px; white-space: nowrap; }

  /* back */
  .services__frame {
    position: absolute; left: 50px; top: 48px; width: 750px; height: 391px;
    border: 2px solid var(--frame-line);
  }
  .services__title {
    position: absolute; left: 0; right: 0; top: 28px; text-align: center;
    color: var(--white); font-weight: 700; font-size: 30px; letter-spacing: 4px; word-spacing: 12px;
  }
  .services__title span { background: var(--card-panel); padding: 0 26px; }
  .service-list { position: absolute; list-style: none; }
  .service-list--left { left: 98px; top: 78px; }
  .service-list--right { left: 538px; top: 96px; }
  .service { display: flex; align-items: center; height: 44px; }
  .service__tick { width: 30px; height: 30px; flex: none; }
  .service__label { margin-left: 16px; color: var(--green); font-size: 27px; white-space: nowrap; }
</style>
</head>
<body>
<svg width="0" height="0" style="position:absolute">
  <defs>
    <symbol id="tick-box" viewBox="0 0 30 30">
      <path d="M24 14v11H4V5h14" fill="none" stroke="#fff" stroke-width="3.5" stroke-linejoin="round"/>
      <path d="M9 14l5 6L28 3" fill="none" stroke="#fff" stroke-width="4" stroke-linecap="round" stroke-linejoin="round"/>
    </symbol>
  </defs>
</svg>

<section class="card card--front">
  <div class="card__panel"></div>
  <div class="brand">
    <div class="brand__name"><span>KRAVEL</span><span class="brand__dot"></span></div>
    <div class="brand__tagline">CONSTRUCTION LTD</div>
  </div>
  <div class="person">
    <div class="person__name">TOMAS VERBELK</div>
    <div class="person__title">MANAGING DIRECTOR</div>
  </div>
  <ul class="contacts">
    <li class="contact">
      <span class="contact__icon"><svg width="18" height="26" viewBox="0 0 18 26"><rect x="2" y="1" width="14" height="24" rx="2" fill="none" stroke="#fff" stroke-width="2"/><rect x="5" y="4" width="8" height="7" fill="#fff"/><g fill="#fff"><rect x="5" y="14" width="2" height="2"/><rect x="8" y="14" width="2" height="2"/><rect x="11" y="14" width="2" height="2"/><rect x="5" y="18" width="2" height="2"/><rect x="8" y="18" width="2" height="2"/><rect x="11" y="18" width="2" height="2"/></g></svg></span>
      <span class="contact__text">0784 531 9027</span>
    </li>
    <li class="contact">
      <span class="contact__icon"><svg width="24" height="24" viewBox="0 0 24 24"><path d="M6.6 10.8a15 15 0 006.6 6.6l2.2-2.2a1 1 0 011-.25 11.4 11.4 0 003.6.57 1 1 0 011 1V20a1 1 0 01-1 1A17 17 0 013 4a1 1 0 011-1h3.5a1 1 0 011 1 11.4 11.4 0 00.57 3.6 1 1 0 01-.25 1z" fill="#fff"/></svg></span>
      <span class="contact__text">020 5194 6381</span>
    </li>
    <li class="contact">
      <span class="contact__icon"><svg width="26" height="26" viewBox="0 0 26 26"><circle cx="13" cy="13" r="11" fill="none" stroke="#fff" stroke-width="2.5"/><path d="M6 8l4 1 1 4-3 3M15 4l1 4 4 1M14 15l4 1 1 4-4 1z" fill="#fff" stroke="#fff" stroke-width="1.5" stroke-linejoin="round"/></svg></span>
      <span class="contact__text">www.kravel.co.uk</span>
    </li>
    <li class="contact">
      <span class="contact__icon"><svg width="26" height="20" viewBox="0 0 26 20"><rect x="1" y="1" width="24" height="18" rx="2" fill="#fff"/><path d="M2 3l11 9 11-9M2 18l8-7M24 18l-8-7" fill="none" stroke="#3ec44a" stroke-width="1.8"/></svg></span>
      <span class="contact__text">tomas@kravel.co.uk</span>
    </li>
  </ul>
</section>

<section class="card card--back">
  <div class="card__panel"></div>
  <div class="services__frame"></div>
  <h2 class="services__title"><span>OUR SERVICES</span></h2>
  <ul class="service-list service-list--left">
    <li class="service"><svg class="service__tick"><use href="#tick-box"/></svg><span class="service__label">Kitchen Renovations</span></li>
    <li class="service"><svg class="service__tick"><use href="#tick-box"/></svg><span class="service__label">Bathroom Renovations</span></li>
    <li class="service"><svg class="service__tick"><use href="#tick-box"/></svg><span class="service__label">House Renovations</span></li>
    <li class="service"><svg class="service__tick"><use href="#tick-box"/></svg><span class="service__label">Garage Conversions</span></li>
    <li class="service"><svg class="service__tick"><use href="#tick-box"/></svg><span class="service__label">Plumbing &amp; Heating</span></li>
    <li class="service"><svg class="service__tick"><use href="#tick-box"/></svg><span class="service__label">Loft Conversions</span></li>
    <li class="service"><svg class="service__tick"><use href="#tick-box"/></svg><span class="service__label">Conservatories</span></li>
    <li class="service"><svg class="service__tick"><use href="#tick-box"/></svg><span class="service__label">Carpentry</span></li>
  </ul>
  <ul class="service-list service-list--right">
    <li class="service"><svg class="service__tick"><use href="#tick-box"/></svg><span class="service__label">Tiling</span></li>
    <li class="service"><svg class="service__tick"><use href="#tick-box"/></svg><span class="service__label">Electrical</span></li>
    <li class="service"><svg class="service__tick"><use href="#tick-box"/></svg><span class="service__label">Extensions</span></li>
    <li class="service"><svg class="service__tick"><use href="#tick-box"/></svg><span class="service__label">Bricklaying</span></li>
    <li class="service"><svg class="service__tick"><use href="#tick-box"/></svg><span class="service__label">Landscaping</span></li>
    <li class="service"><svg class="service__tick"><use href="#tick-box"/></svg><span class="service__label">Decorating</span></li>
    <li class="service"><svg class="service__tick"><use href="#tick-box"/></svg><span class="service__label">Plastering</span></li>
  </ul>
</section>
</body>
</html>
```